The Battle of the Business Cards - Puns, Pixels, and Prizes

Briefing for Q7 Harbor Business Card Design:

Objective:
To design business cards that represent the vision and mission of Q7 Harbor, a company that aims to create the best remote work experience for people and companies, with a focus on simplicity and ease of use.

Design Elements:

Color Scheme: Blue and White
Font: Modern and Clean
Logo: The Q7 Harbor logo should be prominently displayed on the card.
Vision Statement: "Helping businesses create workplaces where people love to work" should be included on the card.
Mission Statement: "Create the best remote work experience for people and companies" should also be included.
Key Focus: The card should emphasize Q7 Harbor's focus on simplicity and ease of use in its cloud solutions.
Design Concept:
The design of the business card should be simple yet professional. The Q7 Harbor logo should be the focal point of the card, and the blue and white color scheme should be used to create a clean and modern feel that reinforces the idea of simplicity and ease of use. Blue represents trust, professionalism, and reliability, while white represents purity, simplicity, and clarity. The card should feature the vision and mission of the company, with each statement being given equal importance. The font used should be modern and clean, with legibility being a top priority. A tagline could be included that emphasizes the company's focus on simplicity and ease of use, such as "Simplicity at its best" or "Streamlined cloud solutions."

Final Thoughts:
The design of the business card should represent Q7 Harbor's vision and mission while also conveying the message that the company is the choice for those who value simplicity and ease of use in their cloud solutions. The final product should leave a lasting impression on anyone who receives it, and it should convey the professionalism and expertise of Q7 Harbor in helping businesses create workplaces where people love to work. The blue and white color scheme can be a great choice for the Q7 Harbor business card design, and it can help to create a professional and memorable impression on clients and partners while emphasizing the company's focus on simplicity and ease of use.
Updates

Need extra days to review

Target Market(s)

Companies that employ remote workers that work on computers

Industry/Entity Type

SaaS

Contact Information for Business Card

Website: www.q7harbor.net, phone, email, whatsApp, LinkedIn,

Font styles to use
Other font styles liked:
• Main Fonts: Poppins Light, Poppins Medium, Poppins Bold Alternative Fonts (for Sub Headers) Cairo Light, Cairo Regular, Cairo Bold

Colors
0054AA
0677BA
7BADD7
CADEEF
E8F1F8

Requirements
Must have
• See Copy of Q7 harbor Branding - 2021.pdf, Briefing for Q7 Harbor Business Card Design: Objective: To design business cards that represent the vision and mission of Q7 Harbor, a company that aims to create the best remote work experience for people and companies, with a focus on simplicity and ease of use. Design Elements: Color Scheme: Blue and White Font: Modern and Clean Logo: The Q7 Harbor logo should be prominently displayed on the card. Vision Statement: "Helping businesses create workplaces where people love to work" should be included on the card. Mission Statement: "Create the best remote work experience for people and companies" should also be included. Key Focus: The card should emphasize Q7 Harbor's focus on simplicity and ease of use in its cloud solutions. Design Concept: The design of the business card should be simple yet professional. The Q7 Harbor logo should be the focal point of the card, and the blue and white color scheme should be used to create a clean and modern feel that reinforces the idea of simplicity and ease of use. Blue represents trust, professionalism, and reliability, while white represents purity, simplicity, and clarity. The card should feature the vision and mission of the company, with each statement being given equal importance. The font used should be modern and clean, with legibility being a top priority. A tagline could be included that emphasizes the company's focus on simplicity and ease of use, such as "Simplicity at its best" or "Streamlined cloud solutions." Final Thoughts: The design of the business card should represent Q7 Harbor's vision and mission while also conveying the message that the company is the choice for those who value simplicity and ease of use in their cloud solutions. The final product should leave a lasting impression on anyone who receives it, and it should convey the professionalism and expertise of Q7 Harbor in helping businesses create workplaces where people love to work. The blue and white color scheme can be a great choice for the Q7 Harbor business card design, and it can help to create a professional and memorable impression on clients and partners while emphasizing the company's focus on simplicity and ease of use.
Nice to have
• Most of of our competitors treat you like a number, we give a sh!t, we take the time to help people get set up and grow. Think of the Tez vs Korvane commercials from the early 2000s

```html
<!DOCTYPE html>
<html lang="en">
<head>
<meta charset="utf-8">
<title>Q7 Harbor Business Cards</title>
<link rel="stylesheet" href="https://fonts.googleapis.com/css2?family=Poppins:wght@300;400;600&family=Cairo:wght@700&display=swap">
<style>
  :root {
    --bg: #d9d9d9;
    --card: #ffffff;
    --blue: #1a78c2;
    --blue-deep: #0054aa;
    --blue-light: #7badd7;
    --orange: #f5a300;
  }
  html, body {
    margin: 0;
    padding: 0;
    width: 1200px;
    height: 846px;
    overflow: hidden;
    background: var(--bg);
    font-family: "Poppins", sans-serif;
  }
  .canvas { position: relative; width: 1200px; height: 846px; }
  .card {
    position: absolute;
    left: 346px;
    width: 508px;
    height: 290px;
    background: var(--card);
  }
  .card--front { top: 99px; }
  .card--back { top: 456px; }

  .brand {
    position: absolute;
    display: flex;
    flex-direction: column;
    align-items: center;
  }
  .brand__mark {
    width: 88px;
    height: 88px;
    border-radius: 50%;
    background: var(--blue-deep);
  }
  .brand__name {
    margin-top: 12px;
    font-weight: 600;
    font-size: 23px;
    line-height: 1;
    color: var(--blue);
    letter-spacing: -0.3px;
    white-space: nowrap;
  }
  .card--front .brand { left: 98px; top: 92px; width: 130px; }
  .card--back .brand { left: 0; right: 0; top: 32px; }

  .contact-list {
    position: absolute;
    left: 238px;
    top: 106px;
    margin: 0;
    padding: 0;
    list-style: none;
  }
  .contact-list li {
    display: flex;
    align-items: center;
    height: 22.2px;
    font-weight: 300;
    font-size: 15px;
    color: var(--blue);
  }
  .contact-list svg {
    width: 18px;
    height: 18px;
    margin-right: 6px;
    flex: none;
  }

  .rule {
    position: absolute;
    left: 88px;
    width: 333px;
    top: 161px;
    height: 0;
    border-top: 1.5px solid var(--orange);
  }
  .tagline {
    position: absolute;
    left: 0;
    right: 0;
    top: 163px;
    margin: 0;
    text-align: center;
    font-weight: 300;
    font-size: 24.5px;
    color: var(--blue);
  }
  .statement {
    position: absolute;
    top: 208px;
    width: 180px;
    text-align: center;
  }
  .statement--vision { left: 71px; }
  .statement--mission { left: 250px; }
  .statement h3 {
    margin: 0 0 2px;
    font-family: "Cairo", sans-serif;
    font-weight: 700;
    font-size: 11.5px;
    line-height: 1.2;
    color: var(--orange);
    letter-spacing: -0.2px;
  }
  .statement p {
    margin: 0;
    font-weight: 300;
    font-size: 11.5px;
    line-height: 14px;
    color: var(--blue);
    white-space: nowrap;
  }
  .quote-mark { color: var(--orange); font-style: italic; font-weight: 600; }
</style>
</head>
<body>
<div class="canvas">

  <section class="card card--front" aria-label="Card front">
    <div class="brand">
      <span class="brand__mark" aria-hidden="true"></span>
      <span class="brand__name">Q7 Harbor</span>
    </div>
    <ul class="contact-list">
      <li>
        <svg viewBox="0 0 24 24" aria-hidden="true"><path fill="var(--blue)" d="M6.6 2.5c.6-.3 1.3-.1 1.6.5l2 3.8c.3.6.1 1.2-.4 1.6l-1.5 1.1c.9 2.6 2.4 4.9 4.4 6.7l1.5-1c.5-.4 1.2-.3 1.6.2l2.6 3.3c.4.5.3 1.3-.2 1.7l-1.4 1.1c-1 .8-2.5.9-3.6.1C8.6 18.6 5.2 13 4.5 6.8c-.1-1.2.5-2.5 1.6-3.1z"/></svg>
        1-800-555-0142
      </li>
      <li>
        <svg viewBox="0 0 24 24" aria-hidden="true"><path d="M4 4h16a1.5 1.5 0 0 1 1.5 1.5v10A1.5 1.5 0 0 1 20 17H10l-5 4v-4H4a1.5 1.5 0 0 1-1.5-1.5v-10A1.5 1.5 0 0 1 4 4z" fill="none" stroke="var(--blue)" stroke-width="2" stroke-linejoin="round"/><circle cx="8" cy="10.5" r="1.3" fill="var(--blue)"/><circle cx="12" cy="10.5" r="1.3" fill="var(--blue)"/><circle cx="16" cy="10.5" r="1.3" fill="var(--blue)"/></svg>
        1-800-555-0142
      </li>
      <li>
        <svg viewBox="0 0 24 24" aria-hidden="true"><rect x="2" y="5" width="20" height="14" fill="var(--blue)"/><path d="M2.5 5.5 12 13l9.5-7.5M2.5 18.5 9.5 11.5M21.5 18.5l-7-7" fill="none" stroke="#fff" stroke-width="1.3"/></svg>
        info@q7harbor.net
      </li>
      <li>
        <svg viewBox="0 0 24 24" aria-hidden="true"><g fill="none" stroke="var(--blue)" stroke-width="2" stroke-linecap="round"><path d="M10 14a4.5 4.5 0 0 0 6.4 0l3.2-3.2a4.5 4.5 0 0 0-6.4-6.4l-1.2 1.2"/><path d="M14 10a4.5 4.5 0 0 0-6.4 0l-3.2 3.2a4.5 4.5 0 0 0 6.4 6.4l1.2-1.2"/></g></svg>
        #Linkora/q7harbor
      </li>
      <li>
        <svg viewBox="0 0 24 24" aria-hidden="true"><circle cx="12" cy="12" r="10" fill="var(--blue)"/><g fill="none" stroke="#fff" stroke-width="1.2"><ellipse cx="12" cy="12" rx="4.5" ry="10"/><path d="M12 2v20M2 12h20M3.5 7h17M3.5 17h17"/></g></svg>
        www.q7harbor.net
      </li>
    </ul>
  </section>

  <section class="card card--back" aria-label="Card back">
    <div class="brand">
      <span class="brand__mark" aria-hidden="true"></span>
      <span class="brand__name">Q7 Harbor</span>
    </div>
    <div class="rule"></div>
    <p class="tagline">Streamlined cloud solutions.</p>
    <div class="statement statement--vision">
      <h3>VISION STATEMENT:</h3>
      <p><span class="quote-mark">"</span>Helping businesses create<br>workplaces where people<br>love to work<span class="quote-mark">"</span></p>
    </div>
    <div class="statement statement--mission">
      <h3>MISSION STATEMENT:</h3>
      <p><span class="quote-mark">"</span>Create the best remote work<br>experience for people<br>and companies<span class="quote-mark">"</span></p>
    </div>
  </section>

</div>
</body>
</html>
```